Eye-catching Yellow Page Ad for Attorney's Office

We need a phone book advertisement for our law office. We practice workers' compensation law, and our clientele consists exclusively of individuals who have been injured on the job. The dimensions of the print ad will be 6" W X 4.54" H.

We've had our current ad for several years, and wanted to get a new one that has been designed by a professional. Being that it's an ad for a law firm, it needs to be professional looking, but we're hoping to have something that looks a little more modern and has eye-catching appeal. We like the text that is included in the ad, and we want to make sure our phone number is very visible. No real preference for color scheme.

I've attached a copy of our current ad. All the information included in there is accurate. Our office name is Thornbury & Lisle, PLLC. The ethical rules for attorney advertising require the PLLC to be included in the ad, but it can be smaller than the other text (see our current ad).

Target Market(s)

Our potential clients are injured workers looking for legal representation in their workers' compensation claim.

Industry/Entity Type

Attorney

Font styles to use
Serif
Sans Serif

Requirements
Must have
• Professional, but stands out from the crowd
Nice to have
• Clean modern design
Should not have
• We don't want it to be too crowded or over-worked.

```html
<!DOCTYPE html>
<html lang="en">
<head>
<meta charset="utf-8">
<title>Thornbury &amp; Lisle, PLLC — Workers' Compensation</title>
<link rel="stylesheet" href="https://fonts.googleapis.com/css2?family=Arimo:wght@400;700&family=Roboto+Condensed:wght@700&display=swap">
<style>
  :root {
    --navy: #1d2f5e;
    --navy-deep: #17264d;
    --sky-top: #29b8ec;
    --sky-mid: #a9dcf5;
    --sky-low: #d6effb;
    --accent-blue: #2a6fba;
    --bullet: #2a78c4;
    --ink: #141414;
    --white: #ffffff;
    --wood-dark: #5a2e14;
    --wood-light: #b9743f;
  }
  * { box-sizing: border-box; margin: 0; padding: 0; }
  html, body { width: 1200px; height: 908px; overflow: hidden; background: var(--white); }
  .ad {
    position: relative; width: 1200px; height: 908px; overflow: hidden;
    font-family: "Arimo", Arial, sans-serif; color: var(--ink); background: var(--white);
  }
  .firm-name {
    position: absolute; top: 22px; left: 0; width: 100%; text-align: center;
    font-weight: 700; font-size: 62px; color: var(--navy); letter-spacing: 1px;
  }
  .firm-name .suffix { font-size: 20px; vertical-align: 34px; margin-left: 8px; }
  .practice-band {
    position: absolute; top: 122px; left: 0; width: 100%; height: 94px;
    background: var(--navy); color: var(--white);
    display: flex; align-items: center; justify-content: center;
    font-weight: 700; font-size: 62px; letter-spacing: 5px;
  }
  .sky {
    position: absolute; top: 219px; left: 0; width: 100%; height: 598px;
    background: linear-gradient(180deg, var(--sky-top) 0%, var(--sky-mid) 28%, var(--sky-low) 60%, #e8f6fd 85%, #4fc0ec 100%);
  }
  .gavel-art {
    position: absolute; top: 362px; left: 752px; width: 360px; height: 300px;
    background: radial-gradient(ellipse at 45% 45%, var(--wood-light) 0%, #8a4a22 45%, var(--wood-dark) 68%, rgba(90,46,20,0) 71%);
  }
  .tagline {
    position: absolute; top: 242px; left: 74px; white-space: nowrap;
    font-family: "Roboto Condensed", "Arial Narrow", sans-serif; font-weight: 700; font-size: 43.5px; color: var(--white);
  }
  .intro {
    position: absolute; top: 298px; left: 74px; width: 1100px;
    font-size: 26px; line-height: 36px; color: var(--ink); white-space: nowrap;
  }
  .help-heading {
    position: absolute; top: 394px; left: 74px;
    font-family: "Roboto Condensed", "Arial Narrow", sans-serif; font-weight: 700; font-size: 45px; color: var(--accent-blue);
  }
  .services { position: absolute; top: 452px; left: 78px; list-style: none; }
  .services li {
    position: relative; padding-left: 40px; font-size: 38.5px; line-height: 47px; color: var(--ink); white-space: nowrap;
  }
  .services li::before {
    content: ""; position: absolute; left: 0; top: 16px; width: 18px; height: 18px;
    border-radius: 50%; background: var(--bullet);
  }
  .values-tab {
    position: absolute; top: 664px; left: 542px; width: 680px; height: 52px;
    background: var(--white); border-top-left-radius: 16px;
    display: flex; align-items: center; padding-left: 46px;
    font-size: 26px; color: var(--navy); letter-spacing: 0.3px; white-space: nowrap;
  }
  .values-tab .sep { color: var(--bullet); margin: 0 7px; }
  .phone-panel {
    position: absolute; top: 712px; left: 550px; width: 660px; height: 105px;
    background: var(--navy); border-top-left-radius: 14px; color: var(--white);
    font-weight: 700; padding-left: 32px; display: flex; align-items: baseline; padding-top: 2px;
    white-space: nowrap;
  }
  .phone-panel .area { font-size: 50px; }
  .phone-panel .number { font-size: 100px; }
  .base-stripe { position: absolute; top: 817px; left: 0; width: 100%; height: 6px; background: var(--white); }
  .contact-bar {
    position: absolute; top: 823px; left: 0; width: 100%; height: 85px;
    background: var(--navy-deep); color: var(--white);
  }
  .address {
    position: absolute; top: 22px; left: 62px; white-space: nowrap;
    font-weight: 700; font-size: 30px;
  }
  .divider { position: absolute; top: 8px; left: 643px; width: 1px; height: 48px; background: var(--white); }
  .website { position: absolute; top: 16px; left: 668px; font-weight: 700; font-size: 35px; letter-spacing: 0.5px; white-space: nowrap; }
</style>
</head>
<body>
<div class="ad">
  <div class="firm-name">Thornbury &amp; Lisle<span class="suffix">PLLC</span></div>
  <div class="practice-band">WORKERS’ COMPENSATION</div>
  <div class="sky"></div>

  <div class="gavel-art" role="img" aria-label="Wooden judge's gavel resting on its sound block"></div>

  <h2 class="tagline">Former Assistant Attorneys General Who Know The System</h2>
  <p class="intro">At Thornbury &amp; Lisle, we provide personal attention to our clients, that means<br>your case is handled by an attorney, not an assitant.</p>

  <h3 class="help-heading">We can help with:</h3>
  <ul class="services">
    <li>Workplace Injuries or Death</li>
    <li>Lost Wages</li>
    <li>Medical Expensese &amp; Treatment</li>
    <li>Hearing Loss Claims</li>
    <li>Pension Claims</li>
    <li>Disability Awards</li>
    <li>Return To Work Issues</li>
  </ul>

  <div class="values-tab">PROFESSIONAL<span class="sep">|</span>COMMITTER<span class="sep">|</span>EFFECTIVE</div>
  <div class="phone-panel"><span class="area">0360</span><span class="number">555-0147</span></div>

  <div class="base-stripe"></div>
  <div class="contact-bar">
    <div class="address">482 W. Harbor Suite 310, Marlow</div>
    <div class="divider"></div>
    <div class="website">www.thornburylisle.com</div>
  </div>
</div>
</body>
</html>
```